Build a Web page - Dovin Pratchell Homes, LLC - a custom home builder

We are a custom home builder in Wisconsin. Need a basic web page with a home page, About Us, Contact info, Gallery, and Testimonials page. Gallery will probably have sub-pages and each will have about ten pictures or less. I already own the domain and have web hosting through Wix, I just need the site built. Once the page is built I should be able to do the upkeep on it myself. If I need to add pictures or whatever.
Updates

Project Deadline Extended
Reason: I am still looking through designs and will select soon - thank you!

Target Market(s)

Gen X and Millennials who are looking to build a home. Custom built homes - not generic spec homes.

Industry/Entity Type

Home Builder

Number of Pages Required

5+ page

Font styles to use
Sans Serif

Colors
ffffff
ec1f27
000000
9d9d9d

Requirements
Must have
• I have no idea if I want coded or in coded. I'm not sure of the difference and why I would want one over the other.
Nice to have
• We like the following colors - red, black, gray, white.
Should not have
• not a big fan of clip art like hammers, tape measures, etc. Must look professional.

```html
<!DOCTYPE html>
<html lang="en">
<head>
<meta charset="utf-8">
<title>Dovin Pratchell Homes, LLC</title>
<link rel="stylesheet" href="https://fonts.googleapis.com/css2?family=Roboto:ital,wght@0,400;0,500;0,700;1,400&display=swap">
<style>
:root{
  --red:#ec1f27;
  --red-main:#ec3a45;
  --red-soft:#f47a7e;
  --ink:#1d1d1d;
  --grey:#9d9d9d;
  --muted:#555;
  --panel:#f3f3f5;
  --white:#ffffff;
}
*{box-sizing:border-box;margin:0;padding:0}
html,body{width:1200px;height:2171px;overflow:hidden}
body{font-family:"Roboto",Arial,sans-serif;color:var(--ink);background:var(--white);position:relative}

/* hero */
.hero{position:absolute;left:0;top:0;width:1200px;height:544px;
  background:
    radial-gradient(ellipse 190px 150px at 640px 430px,rgba(214,170,150,.95),rgba(214,170,150,0) 100%),
    radial-gradient(ellipse 210px 190px at 780px 190px,rgba(150,120,95,.9),rgba(150,120,95,0) 100%),
    radial-gradient(ellipse 260px 320px at 230px 330px,rgba(232,226,205,.9),rgba(232,226,205,0) 100%),
    linear-gradient(100deg,#a9aca4 0%,#cfcbbd 28%,#9c8878 52%,#5a524d 78%,#2e2b2a 100%)}
.site-nav{position:absolute;left:0;top:0;width:1200px;height:67px;border-bottom:1px solid rgba(255,255,255,.35)}
.brand{position:absolute;left:43px;top:20px;display:flex;align-items:center;gap:10px;color:var(--white);
  font-weight:700;font-size:17px;letter-spacing:.5px}
.brand-mark{width:26px;height:26px;border:2px solid var(--white);border-radius:50%}
.menu{position:absolute;left:359px;top:24px;display:flex;gap:40px;list-style:none}
.menu li{color:var(--white);font-size:15px;font-weight:500}
.nav-actions{position:absolute;left:964px;top:16px;display:flex;gap:8px}
.pill{height:32px;border-radius:16px;border:2px solid var(--white);font-size:13px;display:flex;align-items:center;justify-content:center}
.pill-login{color:var(--white);width:61px;background:rgba(0,0,0,.25)}
.pill-quote{background:var(--white);color:var(--ink);width:122px}

/* intro band */
.intro{position:absolute;left:0;top:544px;width:1200px;height:110px;
  background:linear-gradient(90deg,var(--red-main),var(--red-soft));color:var(--white);text-align:center}
.intro h1{font-size:21px;font-weight:700;margin-top:5px}
.intro .rule{margin:9px 52px 0;border-top:1px dashed rgba(255,255,255,.8)}
.intro p{font-size:12.5px;line-height:19px;margin:19px 80px 0}

.section-title{text-align:center;font-size:21px;font-weight:700;color:var(--ink)}
.section-title span{color:var(--red)}
.section-rule{position:absolute;left:52px;width:1096px;border-top:1px dashed var(--grey)}
.section-rule.red{border-top-color:var(--red)}

/* services */
.services{position:absolute;left:0;top:654px;width:1200px;height:329px;background:var(--panel)}
.services .section-title{position:absolute;top:16px;width:100%}
.services .section-rule{top:57px}
.service{position:absolute;top:132px;width:253px;height:126px}
.service .photo{width:253px;height:126px;border-radius:3px}
.service .icon{position:absolute;left:104px;top:-22px;width:45px;height:45px;border-radius:50%;background:var(--red);
  border:2px solid var(--white);display:flex;align-items:center;justify-content:center}
.service .label{position:absolute;left:10px;top:106px;width:233px;height:42px;border-radius:3px;
  background:linear-gradient(90deg,var(--red-main),var(--red-soft));color:var(--white);font-size:15px;
  display:flex;align-items:center;justify-content:center;box-shadow:0 2px 4px rgba(0,0,0,.15)}

/* gallery */
.gallery{position:absolute;left:0;top:983px;width:1200px;height:273px;background:var(--white)}
.gallery .section-title{position:absolute;top:15px;width:100%}
.gallery .section-rule{top:56px}
.gallery-strip{position:absolute;top:85px;left:0;display:flex}
.gallery-strip div{width:240px;height:160px}

/* testimonials */
.testimonials{position:absolute;left:0;top:1256px;width:1200px;height:394px;background:var(--panel)}
.testimonials .section-title{position:absolute;top:17px;width:100%}
.testimonials .section-rule{top:57px}
.divider-v{position:absolute;left:600px;top:104px;height:218px;border-left:1px dashed var(--red)}
.divider-h{position:absolute;left:52px;top:212px;width:1096px;border-top:1px dashed var(--red)}
.testimonial{position:absolute}
.testimonial p{font-style:italic;font-size:12.5px;line-height:19.5px;color:var(--muted)}
.testimonial cite{display:block;font-style:normal;font-size:12.5px;margin-top:10px;color:var(--ink)}
.testimonial.left{left:56px;width:406px;text-align:right}
.testimonial.right{left:738px;width:410px;text-align:left}
.avatar{position:absolute;width:76px;height:76px;border-radius:50%;
  background:radial-gradient(circle at 50% 45%,#d8c2b0 0%,#a88a76 45%,#4a3a32 100%)}

/* skyline */
.skyline{position:absolute;left:0;top:1650px;width:1200px;height:68px;
  background:linear-gradient(180deg,var(--panel) 0%,rgba(236,58,69,.25) 55%,rgba(236,58,69,.85) 100%)}

/* footer */
.site-footer{position:absolute;left:0;top:1718px;width:1200px;height:453px;
  background:linear-gradient(90deg,var(--red-main),var(--red-soft));color:var(--white)}
.col{position:absolute;top:52px;width:253px}
.col h3{font-size:18px;font-weight:700;margin-bottom:18px}
.col p{font-size:12.5px;line-height:19.5px;margin-bottom:14px}
.col p b{font-weight:700}
.social{display:flex;gap:12px;margin-top:4px}
.social span{width:14px;height:14px;border-radius:50%;background:var(--white)}
.field{position:absolute;background:var(--white);border-radius:3px;font-size:12px;color:#888;padding:8px 9px}
.send{position:absolute;left:0;top:228px;width:135px;height:33px;background:var(--white);border-radius:3px;
  color:var(--ink);font-size:13px;display:flex;align-items:center;justify-content:center;letter-spacing:.3px}
.map{position:absolute;left:0;top:42px;width:253px;height:224px;
  background:linear-gradient(120deg,#8fbad4 0%,#a9c8d8 25%,#e6e6df 45%,#efeee8 65%,#c4d9b2 85%,#aecd98 100%)}
.footer-rule{position:absolute;left:52px;top:382px;width:1096px;border-top:1px solid rgba(255,255,255,.5)}
.copyright{position:absolute;top:410px;width:100%;text-align:center;font-size:12px;font-weight:700}
</style>
</head>
<body>

<header class="hero" role="img" aria-label="Photo of a hand holding a small model house in front of a blurred home">
  <nav class="site-nav">
    <div class="brand"><span class="brand-mark"></span>DOVIN PRATCHELL HOMES</div>
    <ul class="menu">
      <li>HOME</li><li>ABOUT US</li><li>SERVICES</li><li>GALLERY</li><li>CONTACT</li>
    </ul>
    <div class="nav-actions">
      <span class="pill pill-login">Log In</span>
      <span class="pill pill-quote">Request a Quote</span>
    </div>
  </nav>
</header>

<section class="intro">
  <h1>Dovin Pratchell Homes, LLC</h1>
  <div class="rule"></div>
  <p>Warehouse construction, tenant improvements and renovations. We provide skilled workmanship from concrete formwork, to tilt up construction, wood and steel framing and any type of finishing or millwork.</p>
</section>

<section class="services">
  <h2 class="section-title">Our <span>Services</span></h2>
  <div class="section-rule"></div>

  <div class="service" style="left:52px">
    <div class="photo" role="img" aria-label="Empty office interior with tall glass windows" style="background:linear-gradient(100deg,#2e5568 0%,#6f9fb6 30%,#c9dde6 55%,#8aa9b4 75%,#3d4d52 100%)"></div>
    <div class="icon"><svg width="20" height="20" viewBox="0 0 20 20" fill="none" stroke="#fff" stroke-width="2"><rect x="3" y="3" width="12" height="5" rx="1"/><path d="M15 5.5h2v5H10v3"/><rect x="8.5" y="13" width="3" height="5"/></svg></div>
    <div class="label">Tenant Improvement</div>
  </div>

  <div class="service" style="left:333px">
    <div class="photo" role="img" aria-label="Steel warehouse frame under construction with cranes" style="background:linear-gradient(180deg,#4f86c2 0%,#a9c6e2 35%,#5d6670 60%,#c9a93a 78%,#6b5b42 100%)"></div>
    <div class="icon"><svg width="20" height="20" viewBox="0 0 20 20" fill="none" stroke="#fff" stroke-width="2"><path d="M2 9l8-6 8 6v9H2z"/><path d="M7 18v-6h6v6"/></svg></div>
    <div class="label">Warehouse Construction</div>
  </div>

  <div class="service" style="left:614px">
    <div class="photo" role="img" aria-label="Bright room being renovated with a wooden ladder" style="background:linear-gradient(100deg,#f1e6d2 0%,#dcc29a 35%,#c48a4a 60%,#e7d3b3 80%,#a8743e 100%)"></div>
    <div class="icon"><svg width="20" height="20" viewBox="0 0 20 20" fill="none" stroke="#fff" stroke-width="2"><path d="M3 17l8-8"/><path d="M11 9a4 4 0 1 0 4-6l-2 3-2-1"/><path d="M12 13l4 4"/></svg></div>
    <div class="label">Renovations</div>
  </div>

  <div class="service" style="left:895px">
    <div class="photo" role="img" aria-label="Two workers in hard hats in front of a steel structure" style="background:linear-gradient(100deg,#3d6f9e 0%,#9fb8cc 40%,#e0822c 65%,#f0c23a 80%,#55606a 100%)"></div>
    <div class="icon"><svg width="20" height="20" viewBox="0 0 20 20" fill="#fff"><path d="M5 8a5 5 0 0 1 10 0z"/><circle cx="10" cy="11" r="2.5"/><path d="M4 19a6 6 0 0 1 12 0z"/></svg></div>
    <div class="label">Project Management</div>
  </div>
</section>

<section class="gallery">
  <h2 class="section-title">Our <span>Gallery</span></h2>
  <div class="section-rule red"></div>
  <div class="gallery-strip">
    <div role="img" aria-label="Two-story home with grey siding" style="background:linear-gradient(180deg,#e4e8ec 0%,#9a9488 30%,#6f675d 60%,#4d5a34 85%,#3b4a26 100%)"></div>
    <div role="img" aria-label="Single-story home with a green lawn" style="background:linear-gradient(180deg,#e2e4e4 0%,#c2b49d 35%,#8c7a62 55%,#6e9a3c 75%,#4e7a26 100%)"></div>
    <div role="img" aria-label="Interior wooden staircase beside a door" style="background:linear-gradient(90deg,#ede8de 0%,#c9b8a2 25%,#8a4a2a 50%,#d7cfc2 70%,#7a4a2a 100%)"></div>
    <div role="img" aria-label="Two-story home with a front porch" style="background:linear-gradient(180deg,#dfe9f2 0%,#c9b6a0 30%,#8e6a5a 55%,#7a8f52 80%,#4f6e2c 100%)"></div>
    <div role="img" aria-label="Home on a green hillside under a blue sky" style="background:linear-gradient(180deg,#4f8fd6 0%,#a8c8ea 35%,#7f8f6a 55%,#6fa43a 75%,#4f8a26 100%)"></div>
  </div>
</section>

<section class="testimonials">
  <h2 class="section-title">What <span>People Say</span></h2>
  <div class="section-rule"></div>
  <div class="divider-v"></div>
  <div class="divider-h"></div>

  <blockquote class="testimonial left" style="top:102px">
    <p>Duis aute irure dolor in reprehenderit in voluptate velit esse cillum dolore eu fugiat nulla pariatur. Excepteur sint occaecat cupidatat non proident, sunt in culpa qui officia deserunt mollit.</p>
    <cite>Owen Farris, Operations Manager</cite>
  </blockquote>
  <div class="avatar" role="img" aria-label="Portrait of a client" style="left:490px;top:103px"></div>

  <div class="avatar" role="img" aria-label="Portrait of a client" style="left:632px;top:103px"></div>
  <blockquote class="testimonial right" style="top:102px">
    <p>Provident, similique sunt in culpa qui officia deserunt mollitia animi, id est laborum et dolorum fuga. Et harum quidem rerum facilis est et expedita distinctio. Nam libero tempore, cum soluta nobis.</p>
    <cite>Nora Velling, Creative Designer</cite>
  </blockquote>

  <blockquote class="testimonial left" style="top:240px">
    <p>Luis aute irure dolor in reprehenderit in piluptate velit esse cillum dolore eu fugiat nulla pariatur. Excepteur sint occaecat cupidatat non proident, sunt in culpa qui officia deserunt mollit.</p>
    <cite>Clara Boden, Manager</cite>
  </blockquote>
  <div class="avatar" role="img" aria-label="Portrait of a client" style="left:490px;top:241px"></div>

  <div class="avatar" role="img" aria-label="Portrait of a client" style="left:632px;top:241px"></div>
  <blockquote class="testimonial right" style="top:240px">
    <p>At vero eos et accusamus et iusto odio dignissimos ducimus qui blanditiis praesentium voluptatum deleniti atque corrupti quos dolores et quas molestias excepturi sint occaecati asperiores.</p>
    <cite>Evan Mirek, Developer</cite>
  </blockquote>
</section>

<div class="skyline" role="img" aria-label="City skyline and airport silhouette"></div>

<footer class="site-footer">
  <div class="col" style="left:52px">
    <h3>Contact Us</h3>
    <p>Please feel free to contact us for any issue. Our staff is available to you from 9AM until 5PM on weekdays.</p>
    <p><b>Phone:</b> +1 (920) 555 0147</p>
    <p><b>Office:</b> Harborline Design Center</p>
    <p><b>Email:</b> hello@pratchellhomes.example</p>
    <div class="social"><span></span><span></span><span></span><span></span><span></span></div>
  </div>

  <div class="col" style="left:333px">
    <h3>Feel Free to Mail</h3>
    <div class="field" style="left:0;top:41px;width:117px;height:32px">Name *</div>
    <div class="field" style="left:136px;top:41px;width:117px;height:32px">Email *</div>
    <div class="field" style="left:0;top:93px;width:253px;height:30px">Subject</div>
    <div class="field" style="left:0;top:144px;width:253px;height:63px">Write Your Message Here...</div>
    <div class="send">SEND MESSAGE</div>
  </div>

  <div class="col" style="left:614px">
    <h3>Headquarters</h3>
    <div class="map" role="img" aria-label="Street map showing the office location"></div>
  </div>

  <div class="col" style="left:895px">
    <h3>About Team</h3>
    <p>Enim congue blandit. Lorem ipsum dolor sit amet, consectetur adipiscing elit. Quisque consectetur interdum finibus. Vestibulum ante ipsum primis in faucibus orci. luctus et ultrices posuere.</p>
    <p>Cubilia cras blandit finibus ipsum, id porttitor arcu volutpat a. Integer iaculis erat nec justo malesuada faucibus vel tempus sapien. Vivamus aliquam euismod tristique.</p>
  </div>

  <div class="footer-rule"></div>
  <p class="copyright">Copyright © Dovin Pratchell Homes, LLC All rights reserved</p>
</footer>

</body>
</html>
```